Core Values poster for display in office

We want to create a poster that displays our core values which we can print and place in our office and potentially use on our website.

DataHaven is a Cyber Security consultancy that helps its secure its clients from Cyber Criminals.

Our core values are what we live and breath everyday. They are:
- Customer love
- High performing team
- Do the right thing
- An awesome culture
- Innovative

Here they are again with more detail after each:
- Customer love – exchange in abundance
- High performing team – do whatever it takes, no passengers
- Do the right thing – be accountable, maintain our integrity
- An awesome culture – work hard, play hard, collaborate and celebrate success
- Innovative – solving problems with new ideas

We are in the process of rolling out new branding with a load of comic book style super hero's and villains. Attached are some of those images in PDF format for some business card designs for you to review if you want to incorporate, but I will upload these images to this dropbox folder once my designer sends them to me:
https://www.filecrate-share.net/sh/qpwlzrtkc42hbum/XKPq9LmVtR3sDwYuNHaEfG81b?dl=0

I stumbled across another business with the same name as us and saw their values poster, which I liked conceptually.
www.datahaven-example.net
I've attached the image for reference (note this is not our business or values - just saying I like the concept).

Also attached is our logo in EPS format.

We would like the image editing version of the file once complete so we can edit the file in case we change or tweak our values in the near future.

Target Market(s)

This poster is to be displayed internally and maybe on our website in the hiring section

Industry/Entity Type

Office

Colors
0792cd
ffffff
f68e4e
e667a6
fbee3e

Requirements
Must have
• Must have a vibrant, impactful poster that clearly states our core values in a way so that they are understood.
• Must be print ready in high definition (large A2 size poster).
Nice to have
• Integrate our logo

```html
<!DOCTYPE html>
<html lang="en">
<head>
<meta charset="utf-8">
<title>DataHaven Core Values – Innovative</title>
<link rel="stylesheet" href="https://fonts.googleapis.com/css2?family=Arimo:wght@400;700&display=swap">
<style>
  :root {
    --page-bg: #e7e7e7;
    --white: #ffffff;
    --ink: #3a3a3c;
    --brand-blue: #0792cd;
    --edge-plum: #8b1f5c;
    --glow-yellow: #fbd43e;
    --warm-orange: #f39431;
    --deep-red: #e5262c;
  }
  * { box-sizing: border-box; margin: 0; padding: 0; }
  html, body {
    width: 1200px; height: 856px; overflow: hidden;
    background: var(--page-bg);
    font-family: "Arimo", Arial, sans-serif;
  }
  .poster {
    position: absolute;
    left: 311px; top: 20px;
    width: 577px; height: 816px;
    overflow: hidden;
    background: radial-gradient(ellipse 70% 62% at 50% 70%,
      var(--glow-yellow) 0%, var(--warm-orange) 48%, var(--deep-red) 100%);
    box-shadow: 0 6px 24px rgba(0,0,0,0.25);
  }
  .poster__header {
    position: absolute; inset: 0;
    width: 100%; height: 100%;
  }
  .brand {
    position: absolute;
    left: 0; right: 0; top: 58px;
    display: flex; align-items: center; justify-content: center; gap: 10px;
  }
  .brand__dot {
    width: 22px; height: 22px; border-radius: 50%;
    background: var(--brand-blue);
  }
  .brand__name {
    font-size: 32px; font-weight: 400; color: var(--ink);
    letter-spacing: 0.2px;
  }
  .value-artwork {
    position: absolute;
    left: 154px; top: 222px; width: 272px; height: 322px;
    border-radius: 46% 46% 40% 40%;
    background: radial-gradient(circle at 50% 40%, rgba(255,255,255,0.95), rgba(255,255,255,0.7) 70%, rgba(255,255,255,0.35));
  }
  .value-title {
    position: absolute; left: 0; right: 0; top: 563px;
    text-align: center;
    font-size: 40px; font-weight: 400; color: var(--white);
    letter-spacing: 1px;
  }
  .values-row {
    position: absolute; left: 0; right: 0; top: 706px;
    list-style: none;
  }
  .values-row__item {
    position: absolute; width: 130px; margin-left: -65px;
    display: flex; flex-direction: column; align-items: center; gap: 8px;
  }
  .values-row__icon {
    width: 44px; height: 44px; border-radius: 50%;
    background: rgba(255,255,255,0.85);
  }
  .values-row__label {
    font-size: 8.5px; color: var(--white); text-transform: uppercase;
    white-space: nowrap;
  }
</style>
</head>
<body>
  <main class="poster">
    <svg class="poster__header" viewBox="0 0 434 615" preserveAspectRatio="none" aria-hidden="true">
      <path d="M0,0 H434 V50 C420,52 405,49 395,58 C384,69 362,72 350,68 C330,61 300,72 280,95 C260,118 238,124 220,123 C190,121 160,100 132,75 C112,57 96,52 82,53 C68,55 58,80 40,95 C25,107 10,112 0,114 Z" fill="var(--white)"/>
      <path d="M434,50 C420,52 405,49 395,58 C384,69 362,72 350,68 C330,61 300,72 280,95 C260,118 238,124 220,123 C190,121 160,100 132,75 C112,57 96,52 82,53 C68,55 58,80 40,95 C25,107 10,112 0,114" fill="none" stroke="var(--edge-plum)" stroke-width="2.5"/>
    </svg>

    <header class="brand">
      <span class="brand__dot"></span>
      <span class="brand__name">DataHaven</span>
    </header>

    <div class="value-artwork" role="img" aria-label="White illustration of a head in profile with arrows bursting outward from the mind and one arrow pointing down"></div>

    <h1 class="value-title">INNOVATIVE</h1>

    <ul class="values-row">
      <li class="values-row__item" style="left:121px">
        <span class="values-row__icon" role="img" aria-label="Icon of two heads facing each other"></span>
        <span class="values-row__label">High performing team</span>
      </li>
      <li class="values-row__item" style="left:236px">
        <span class="values-row__icon" role="img" aria-label="Icon of a heart held in hands"></span>
        <span class="values-row__label">Customer love</span>
      </li>
      <li class="values-row__item" style="left:346px">
        <span class="values-row__icon" role="img" aria-label="Icon of a celebrating figure"></span>
        <span class="values-row__label">An awesome culture</span>
      </li>
      <li class="values-row__item" style="left:479px">
        <span class="values-row__icon" role="img" aria-label="Icon of a target with an arrow"></span>
        <span class="values-row__label">Do the right thing</span>
      </li>
    </ul>
  </main>
</body>
</html>
```